Home and interior page website design for HVAC company - Veltrix Corp.

Create homepage and one interior page website design for an HVAC (Heating and AC) company. Current website is: https://veltrixcorp-example.com/.

Client has specifically asked that the new site look inviting, informative and interactive. They mentioned that the logo on a white background doesn't look appealing and would like to see other options. (I have included the white background one from their current website as well as the one on an image that the client sent me) The site must include their financing widget (we have the code for this) in a prominent place. Image can be found here: https://fundlarkpay-example.com/badges/fundlark-financing.png.

The content from their existing site belongs to the company that built their site and have said we cannot use any of it. This development site (http://veltrixwebd.qmzdev-example.com/) is what we originally created from our template for them before they decided they wanted a custom built site. The content there is what will need to be on the new home page.

We have gathered images from the client that they would like used throughout the site in this folder: https://files.brelvon-example.com/shared/folder/Xk4pQ9wLmZ2rTn7vBc8HyD5sJf3GaE6uWq1NoKi0RtYe?e=7PLWQD. They would like the photos used to be in tune with the topic being spoken about so if the topic is maintenance on a central AC system the photo used to lead that topic should be of a unit being cleaned.

For the testimonials section please also include a button or "Click here for more testimonials" as requested by the client.

Top Level NAV should include: Home, Residential, Commercial, Testimonials, Gallery, About Us, Coupons, Contact Us

For the interior page, we're looking for the same inviting, informative and interactive feel to the site, preferably with a banner of some sort and the form close to the top of the page if not able to keep it above the fold in the banner. Page should also include sections with clients images used to avoid a wall of text.

Example Websites that the client likes:
https://www.corvalheatcoolinc-example.com/
https://www.frostelmg-example.com/?ref=Q8mZt3LpXw2NvB7cRk5YhJ1sDf4GaE9u
https://www.glimtherm-example.com/nny/
https://www.ubrix-example.com/
https://otterclimateny-example.com/

• *Summarized from project description:
-financing image in prominent place
-content from development site
-images from clients folder
-button or "click here.." note in testimonials section
-form above the fold
-logo not on white background

```html
<!DOCTYPE html>
<html lang="en">
<head>
<meta charset="utf-8">
<title>Veltrix Mechanical Contractors Corp — Residential and Commercial HVAC</title>
<link rel="stylesheet" href="https://fonts.googleapis.com/css2?family=Mulish:wght@400;600;700;800&family=Lora:ital@1&display=swap">
<style>
:root{
  --red:#d30b0b;
  --black:#0d0d0d;
  --navy:#2b3747;
  --footer:#2d3b4c;
  --page:#f0f0f0;
  --text:#1e1e1e;
  --white:#ffffff;
}
*{box-sizing:border-box;margin:0;padding:0}
html,body{width:1200px;height:3627px;overflow:hidden}
body{font-family:"Mulish",sans-serif;color:var(--text);background:var(--page)}
.page{position:relative;width:1200px;height:3627px;overflow:hidden;background:linear-gradient(180deg,#f2f2f2 0%,#f7f7f7 40%,#ececec 60%,#f6f6f6 100%)}

/* header */
.site-header{position:absolute;left:0;top:0;width:1200px;height:120px;background:var(--white)}
.topbar-call{position:absolute;left:697px;top:0;width:240px;height:31px;background:var(--black);clip-path:polygon(12% 0,100% 0,100% 100%,0 100%);color:#fff;font-size:12px;font-weight:700;display:flex;align-items:center;justify-content:center;padding-left:28px}
.topbar-estimate{position:absolute;left:935px;top:0;width:177px;height:31px;background:var(--red);color:#fff;font-size:12px;font-weight:800;display:flex;align-items:center;justify-content:center}
.brand{position:absolute;left:88px;top:30px;display:flex;align-items:center;gap:10px}
.brand-dot{width:40px;height:40px;border-radius:50%;background:var(--black)}
.brand-name{font-size:32px;font-weight:800;color:var(--black);line-height:1}
.brand-sub{position:absolute;left:90px;top:81px;font-size:11px;font-weight:700;color:var(--black);letter-spacing:.6px}
.main-nav a{position:absolute;top:68px;font-size:12.5px;font-weight:700;color:#222;text-decoration:none}
.main-nav a.active{color:var(--red)}

/* hero */
.hero-photo{position:absolute;left:0;top:120px;width:1200px;height:700px;clip-path:polygon(0 0,100% 0,100% 74%,0 100%);
  background:
    radial-gradient(ellipse 260px 120px at 720px 470px,rgba(240,150,70,.55),transparent 70%),
    radial-gradient(ellipse 320px 140px at 260px 520px,rgba(230,120,90,.45),transparent 70%),
    radial-gradient(ellipse 300px 120px at 1040px 520px,rgba(210,140,90,.4),transparent 70%),
    linear-gradient(180deg,#3b4d70 0%,#2a3552 25%,#3d3b5e 45%,#2a2438 62%,#1b1a28 100%)}
.hero-title{position:absolute;left:88px;top:300px;color:#fff;font-size:39px;font-weight:700}
.hero-sub{position:absolute;left:88px;top:354px;color:#fff;font-size:23px;font-weight:400}
.pill{position:absolute;border-radius:20px;font-weight:800;display:flex;align-items:center;justify-content:center;text-decoration:none}
.pill-red{background:var(--red);color:#fff}
.pill-black{background:var(--black);color:#fff}
.pill-white{background:#fff;color:var(--red)}

.consult{position:absolute;left:824px;top:196px;width:288px;height:367px;background:rgba(190,195,205,.85)}
.consult-card{position:absolute;left:17px;top:15px;width:254px;height:335px;background:#fff}
.consult-head{position:absolute;left:0;top:0}
.consult-title{position:absolute;left:0;top:16px;width:254px;text-align:center;color:#fff;font-size:15px;font-weight:700}
.field{position:absolute;left:15px;width:224px;height:32px;background:#ececec;font-size:12px;color:#333;display:flex;align-items:center;padding-left:15px}
.field svg{position:absolute;right:12px;top:12px}
.submit{left:71px;top:289px;width:112px;height:30px;font-size:12px}

.services-head{position:absolute;left:0;top:570px;width:1200px;text-align:center;color:#fff;font-size:19px;font-weight:700}
.services-chev{position:absolute;left:593px;top:598px}
.service-card{position:absolute;top:641px;width:233px;height:200px;overflow:hidden}
.service-photo{position:absolute;inset:0}
.service-label{position:absolute;left:0;bottom:0;width:233px;height:31px;background:rgba(55,62,78,.92);clip-path:polygon(0 0,78% 0,100% 100%,0 100%);color:#fff;font-size:14px;font-weight:700;padding:7px 0 0 15px}
.service-label.hot{background:var(--red)}

/* about */
.about-shade{position:absolute;left:108px;top:841px;width:600px;height:254px;background:#e2e2e2}
.about-card{position:absolute;left:208px;top:921px;width:479px;height:480px;background:var(--red);color:#fff;padding:44px 46px 0 48px}
.about-card h2{font-size:30px;font-weight:800;line-height:1.18;margin-bottom:22px}
.about-lead{font-size:12.5px;font-weight:800;line-height:1.55;margin-bottom:24px;width:370px}
.about-body{font-size:12.5px;line-height:1.55;font-weight:400;width:385px}
.about-photo{position:absolute;left:687px;top:998px;width:304px;height:480px;
  background:
    radial-gradient(ellipse 90px 130px at 150px 200px,rgba(45,60,100,.85),transparent 75%),
    radial-gradient(ellipse 60px 90px at 250px 330px,rgba(170,220,190,.8),transparent 75%),
    radial-gradient(ellipse 110px 70px at 130px 330px,rgba(80,110,160,.7),transparent 75%),
    linear-gradient(180deg,#a9c6e2 0%,#c9d6e0 20%,#b8aea0 45%,#d8cbb0 75%,#c7bda8 100%)}

/* repairs */
.repairs{position:absolute;left:205px;top:1546px;width:790px;text-align:center}
.repairs h2{font-size:32px;font-weight:700;color:#111;margin-bottom:24px}
.repairs p{font-size:14px;line-height:1.4;color:#2a2a2a;margin-bottom:19px}
.repairs strong{font-weight:800}

/* testimonials band */
.dark-band{position:absolute;left:0;top:2084px;width:1200px;height:940px;clip-path:polygon(0 16%,100% 0,100% 84%,0 100%);
  background:radial-gradient(ellipse 500px 300px at 300px 520px,rgba(90,90,90,.55),transparent 70%),radial-gradient(ellipse 400px 260px at 950px 700px,rgba(80,80,80,.5),transparent 70%),linear-gradient(135deg,#343434 0%,#2a2a2a 50%,#383838 100%)}

/* cooling */
.cooling{position:absolute;left:208px;top:1953px;width:488px;height:335px;background:var(--navy);color:#fff;padding:28px 24px}
.cooling h2{font-size:32px;font-weight:700;margin-bottom:12px}
.cooling-sub{font-size:13.5px;line-height:1.35;margin-bottom:20px;width:360px}
.tick-list{list-style:none}
.tick-list li{font-size:13.5px;display:flex;align-items:center;gap:18px;height:24px}
.cooling-photo{position:absolute;left:696px;top:1953px;width:295px;height:335px;
  background:
    radial-gradient(circle 55px at 85px 160px,rgba(60,120,200,.85),transparent 80%),
    radial-gradient(circle 55px at 180px 160px,rgba(210,60,60,.85),transparent 80%),
    radial-gradient(ellipse 30px 120px at 250px 170px,rgba(230,200,40,.7),transparent 80%),
    linear-gradient(170deg,#d7dadd 0%,#b7bcc0 35%,#7f878d 70%,#9a8a6e 100%)}

.clients-title{position:absolute;left:0;top:2356px;width:1200px;text-align:center;color:#fff;font-size:33px;font-weight:700}
.quote-badge{position:absolute;left:556px;top:2428px;width:80px;height:80px;border-radius:50%;background:var(--red);color:#fff;font-size:58px;font-weight:800;text-align:center;line-height:92px}
.quote{position:absolute;left:230px;top:2528px;width:740px;text-align:center;color:#fff;font-family:"Lora",serif;font-style:italic;font-size:14.5px;line-height:24px}
.quote-rule{position:absolute;top:2654px;height:1px;width:140px;background:#888}
.quote-mark{position:absolute;left:585px;top:2643px;color:var(--red);font-size:22px;font-weight:800}
.client-name{position:absolute;left:0;top:2672px;width:1200px;text-align:center;color:var(--red);font-size:14px;font-weight:700}
.slider-dots{position:absolute;left:1102px;top:2530px;display:flex;flex-direction:column;gap:5px}
.slider-dots span{width:9px;height:9px;border:1px solid #bbb;border-radius:50%}

/* cta */
.cta-frame{position:absolute;left:127px;top:2867px;width:457px;height:343px;background:var(--red);border-radius:0 0 0 20px}
.cta-photo{position:absolute;left:87px;top:2867px;width:480px;height:326px;border-radius:0 0 16px 16px;
  background:
    radial-gradient(ellipse 120px 140px at 290px 190px,rgba(225,190,150,.8),transparent 75%),
    radial-gradient(ellipse 160px 110px at 120px 80px,rgba(140,170,110,.75),transparent 75%),
    radial-gradient(ellipse 130px 100px at 300px 290px,rgba(110,120,150,.55),transparent 75%),
    linear-gradient(135deg,#dfe6d6 0%,#c7d0b5 35%,#ece4d8 70%,#d8cfc3 100%)}
.cta-text{position:absolute;right:88px;top:2993px;text-align:right;color:#1b1b1b;font-size:24px;line-height:29px}
.cta-text b{font-weight:800}
.cta-call{color:var(--red);font-size:30px;font-weight:700;margin-top:4px;line-height:34px}

/* footer */
.site-footer{position:absolute;left:0;top:3274px;width:1200px;height:353px;background:var(--footer);color:#fff}
.finance-badge{position:absolute;left:89px;top:81px;width:174px;height:78px;background:linear-gradient(180deg,#f7a437,#ef8a2a);border-radius:4px;display:flex;flex-direction:column;align-items:center;justify-content:center}
.finance-badge .fb-name{font-size:24px;font-weight:700;color:#fff}
.finance-badge .fb-sub{font-size:13px;font-weight:700;color:#fff}
.foot-col{position:absolute;top:82px}
.foot-col h3{font-size:17px;font-weight:700;margin-bottom:14px}
.foot-col p,.foot-col a{font-size:12.5px;line-height:19px;color:#fff;text-decoration:none;display:block}
.foot-links{display:grid;grid-template-columns:115px 100px}
.newsletter{position:absolute;left:879px;top:171px;width:233px;height:31px;background:#fff;border-radius:16px;color:#444;font-size:11px;padding:9px 16px}
.newsletter-go{position:absolute;right:5px;top:5px;width:21px;height:21px;border-radius:50%;background:var(--red)}
.foot-rule{position:absolute;left:88px;top:264px;width:1024px;height:1px;background:#4c5a6b}
.copyright{position:absolute;left:88px;top:300px;font-size:12px}
.pay-badges{position:absolute;left:617px;top:294px;display:flex;gap:9px}
.pay-badges span{width:41px;height:25px;background:#fff;border-radius:4px}
.social{position:absolute;top:292px;width:30px;height:30px;border-radius:50%}
</style>
</head>
<body>
<div class="page">

  <header class="site-header">
    <div class="topbar-call">Call Us: (555) 210-4478</div>
    <div class="topbar-estimate">Get a Free Estimate</div>
    <div class="brand"><span class="brand-dot"></span><span class="brand-name">Veltrix</span></div>
    <div class="brand-sub">MECHANICAL CONTRACTORS</div>
    <nav class="main-nav">
      <a class="active" style="left:363px" href="#">Home</a>
      <a style="left:438px" href="#">Residential</a>
      <a style="left:545px" href="#">Commercial</a>
      <a style="left:662px" href="#">Testimonials</a>
      <a style="left:776px" href="#">Gallery</a>
      <a style="left:859px" href="#">About Us</a>
      <a style="left:953px" href="#">Coupons</a>
      <a style="left:1045px" href="#">Contact Us</a>
    </nav>
  </header>

  <div class="hero-photo" role="img" aria-label="City skyline at dusk with a suspension bridge over the river"></div>
  <h1 class="hero-title">Veltrix Mechanical Contractors Corp</h1>
  <p class="hero-sub">Residential and Commercial HVAC Solutions</p>
  <a class="pill pill-red" href="#" style="left:89px;top:418px;width:159px;height:30px;font-size:12px">Contact Us Today!</a>

  <div class="consult">
    <div class="consult-card">
      <svg class="consult-head" width="254" height="80" viewBox="0 0 254 80"><polygon points="0,0 254,0 254,50 127,80 0,50" fill="#0d0d0d"/></svg>
      <div class="consult-title">Get a Free Consultation</div>
      <div class="field" style="top:89px">Name</div>
      <div class="field" style="top:138px">Email</div>
      <div class="field" style="top:189px">Phone No.</div>
      <div class="field" style="top:238px">Services
        <svg width="10" height="7" viewBox="0 0 10 7"><path d="M1 1l4 4 4-4" stroke="#555" stroke-width="1.4" fill="none"/></svg>
      </div>
      <a class="pill pill-black submit" href="#">Submit</a>
    </div>
  </div>

  <div class="services-head">Our Services</div>
  <svg class="services-chev" width="14" height="9" viewBox="0 0 14 9"><path d="M1 1l6 6 6-6" stroke="#fff" stroke-width="1.8" fill="none"/></svg>

  <div class="service-card" style="left:87px">
    <div class="service-photo" role="img" aria-label="Living room with a wall-mounted air conditioner above a sofa" style="background:radial-gradient(ellipse 70px 30px at 140px 30px,rgba(255,255,255,.9),transparent 80%),radial-gradient(ellipse 110px 40px at 110px 140px,rgba(150,140,130,.8),transparent 80%),linear-gradient(180deg,#f1efec 0%,#e3ddd4 45%,#c6bcae 70%,#a99c8b 100%)"></div>
    <div class="service-label">Air Conditioning</div>
  </div>
  <div class="service-card" style="left:352px">
    <div class="service-photo" role="img" aria-label="Technician holding manifold gauges on a heating unit" style="background:radial-gradient(circle 38px at 90px 80px,rgba(60,110,200,.85),transparent 85%),radial-gradient(circle 38px at 150px 90px,rgba(210,60,60,.85),transparent 85%),radial-gradient(ellipse 40px 60px at 210px 40px,rgba(240,200,40,.8),transparent 85%),radial-gradient(ellipse 90px 40px at 140px 180px,rgba(120,220,190,.8),transparent 85%),linear-gradient(160deg,#c8b89a,#a07a5a 55%,#7b6a5e)"></div>
    <div class="service-label hot">Heating</div>
  </div>
  <div class="service-card" style="left:615px">
    <div class="service-photo" role="img" aria-label="Technician repairing an outdoor condenser unit" style="background:radial-gradient(ellipse 50px 60px at 185px 100px,rgba(250,250,250,.95),transparent 80%),radial-gradient(ellipse 70px 60px at 60px 120px,rgba(120,130,140,.8),transparent 80%),radial-gradient(ellipse 40px 40px at 120px 130px,rgba(40,90,170,.7),transparent 85%),linear-gradient(170deg,#e4e7ea,#c2c9cf 50%,#9ea7ae)"></div>
    <div class="service-label">Repairs</div>
  </div>
  <div class="service-card" style="left:880px">
    <div class="service-photo" role="img" aria-label="Work gloves, hoses and gauges in a tool bag" style="background:radial-gradient(ellipse 70px 80px at 60px 80px,rgba(80,100,130,.9),transparent 80%),radial-gradient(ellipse 50px 50px at 150px 130px,rgba(190,50,50,.85),transparent 85%),radial-gradient(circle 30px at 200px 140px,rgba(230,240,245,.9),transparent 85%),radial-gradient(ellipse 60px 40px at 170px 40px,rgba(220,170,120,.8),transparent 85%),linear-gradient(160deg,#5a6a82,#7a6a66 50%,#4d5a6e)"></div>
    <div class="service-label">Serving Your Area</div>
  </div>

  <div class="about-shade"></div>
  <section class="about-card">
    <h2>Local Brooklyn, NY HVAC Contractors</h2>
    <p class="about-lead">Veltrix Mechanical Air Duct, Insulation, Furnace, Air Conditioning repair and replacement company offers top repair services.</p>
    <p class="about-body">We can resolve any issues that may arise within your home. Our Brooklyn HVAC (heating, ventilating, and air conditioning) technicians are experts at inspecting and repairing systems that are not cooling or heating properly. They specialize at everything from condensers, coils, air ducts, air filtration to complete AC installations and AC replacements with the best warranties ...</p>
  </section>
  <a class="pill pill-white" href="#" style="left:256px;top:1324px;width:127px;height:30px;font-size:12px">About Us</a>
  <div class="about-photo" role="img" aria-label="Technician kneeling beside a rooftop unit checking refrigerant pressure"></div>

  <section class="repairs">
    <h2>Professional HVAC Repairs</h2>
    <p>Honesty and integrity are the hallmarks of the Veltrix Mechanical Contractors Corp business philosophy and are the foundation upon which the company was founded.</p>
    <p>We thrive on providing clear explanations to our customers and doing things right the first time. We look forward to serving you and your family for life by providing peace of mind with the best warranties in the business.</p>
    <p>You can count on our analysis of your home's heating and cooling problems as well as our recommendations for installation, and maintenance. We provide state-of-the-art equipment, so all jobs are performed professionally and efficiently. <strong>To schedule an appointment with our furnace and air conditioning repair and installation experts, call (555) 210-4478.</strong></p>
  </section>
  <a class="pill pill-black" href="#" style="left:521px;top:1843px;width:158px;height:31px;font-size:12px">Get Started Now</a>

  <div class="dark-band" role="img" aria-label="Faded photo of a family relaxing together at home"></div>

  <section class="cooling">
    <h2>Air Conditioning &amp; Cooling</h2>
    <p class="cooling-sub">Serving both Resazidential &amp; Commercial Heating &amp; Air Conditioning Needs</p>
    <ul class="tick-list">
      <li><svg width="14" height="14" viewBox="0 0 14 14"><circle cx="7" cy="7" r="6" stroke="#fff" fill="none"/><path d="M4 7l2 2 4-4" stroke="#fff" fill="none" stroke-width="1.3"/></svg>Air Purifier System</li>
      <li><svg width="14" height="14" viewBox="0 0 14 14"><circle cx="7" cy="7" r="6" stroke="#fff" fill="none"/><path d="M4 7l2 2 4-4" stroke="#fff" fill="none" stroke-width="1.3"/></svg>HVAC Maintenance Tune Up and Inspection</li>
      <li><svg width="14" height="14" viewBox="0 0 14 14"><circle cx="7" cy="7" r="6" stroke="#fff" fill="none"/><path d="M4 7l2 2 4-4" stroke="#fff" fill="none" stroke-width="1.3"/></svg>HVAC Parts, Repair, Installation</li>
      <li><svg width="14" height="14" viewBox="0 0 14 14"><circle cx="7" cy="7" r="6" stroke="#fff" fill="none"/><path d="M4 7l2 2 4-4" stroke="#fff" fill="none" stroke-width="1.3"/></svg>HVAC Replacement Cost and Installation</li>
    </ul>
  </section>
  <a class="pill pill-red" href="#" style="left:232px;top:2218px;width:119px;height:30px;font-size:12px">Read More</a>
  <div class="cooling-photo" role="img" aria-label="Blue and red manifold gauges connected to an AC unit"></div>

  <h2 class="clients-title">Happy Clients Say</h2>
  <div class="quote-badge">“</div>
  <blockquote class="quote">“ Thank you so much for doing such a wonderful job on our air conditioning unit.<br>I am very happy with the service provided to me from Veltrix Mechanical Contractors.<br>The staff gathers my information before helping me out to see what they could do for me.<br>I am thankful for all of your help and services.”</blockquote>
  <div class="quote-rule" style="left:435px"></div>
  <div class="quote-rule" style="left:617px"></div>
  <div class="quote-mark">“</div>
  <div class="client-name">Daniel M.</div>
  <a class="pill pill-red" href="#" style="left:465px;top:2729px;width:263px;height:30px;font-size:12px">Click Here for More Testimonials</a>
  <div class="slider-dots"><span></span><span style="background:#bbb"></span><span></span><span></span><span></span></div>

  <div class="cta-frame"></div>
  <div class="cta-photo" role="img" aria-label="Woman relaxing on a sofa looking at her phone"></div>
  <div class="cta-text">
    <b>Day or Night, 24/7,</b><br>
    Count on Trusted Service from<br>
    Veltrix Mechanical Contractors Corp
    <div class="cta-call">Call:&nbsp; (555) 390-1826</div>
  </div>
  <a class="pill pill-black" href="#" style="left:914px;top:3144px;width:198px;height:35px;font-size:12px">Get Started Now</a>

  <footer class="site-footer">
    <div class="finance-badge"><span class="fb-name">FundLark</span><span class="fb-sub">Consumer Financing</span></div>
    <div class="foot-col" style="left:351px">
      <h3>Contact Us</h3>
      <p style="font-size:14px">Call Us: (555) 210-4478</p>
      <p>e. veltrixcorp@example.com</p>
      <p style="margin-top:24px">Address:</p>
      <p>Brooklyn, NY 11299</p>
    </div>
    <div class="foot-col" style="left:615px">
      <h3>Quick Links</h3>
      <div class="foot-links">
        <div><a href="#">Home</a><a href="#">Residential</a><a href="#">Commercial</a><a href="#">Testimonials</a><a href="#">Gallery</a><a href="#">About Us</a></div>
        <div><a href="#">Coupons</a><a href="#">Contact Us</a></div>
      </div>
    </div>
    <div class="foot-col" style="left:879px">
      <h3>Sign Up Newsletter</h3>
      <p style="font-size:11.5px;line-height:18px;width:240px">There are many variations of passages lorem Ipsum available</p>
    </div>
    <div class="newsletter">Enter your email ...<span class="newsletter-go"></span></div>
    <div class="foot-rule"></div>
    <div class="copyright">©2021 Veltrix Mechanical Contractors. All Right Reserved</div>
    <div class="pay-badges"><span></span><span></span><span></span><span></span><span></span><span></span></div>
    <span class="social" style="left:982px;background:#fff"></span>
    <span class="social" style="left:1021px;background:var(--red)"></span>
  </footer>

</div>
</body>
</html>
```